Modern Lawfirm Business Card Design

We're looking for a business card to incorporate the newly created logo we had made.

Ideally looking for a law firm business card demonstrating, modern, minimalist, strong/bold design.

I'm open to any design honestly, but nothing "flashy".

Target Market(s)

Immigration law, family immigration, humanitarian, general legal

Industry/Entity Type

Law Firm

Contact Information for Business Card

Please use dummy information, name, street address, city, state, phone number, email, website.

Font styles to use
Serif
Sans Serif

Requirements
Must have
• Please use dummy information, name, street address, city, state, phone number, email, website.

```html
<!DOCTYPE html>
<html lang="en">
<head>
<meta charset="utf-8">
<title>Alvero Immigration Law – Business Card</title>
<link rel="stylesheet" href="https://fonts.googleapis.com/css2?family=Source+Serif+4:wght@400;600&display=swap">
<style>
  :root {
    --brand-blue: #1f4a85;
    --brand-blue-dark: #1b4079;
    --card-white: #f7f7f7;
    --text-grey: #4a4a4a;
    --backdrop: #e4e4e4;
  }
  * { margin: 0; padding: 0; box-sizing: border-box; }
  html, body { width: 1200px; height: 576px; overflow: hidden; }
  body {
    background: var(--backdrop);
    position: relative;
    font-family: "Source Serif 4", Georgia, serif;
  }
  .card {
    position: absolute;
    width: 484px;
    height: 292px;
    border-radius: 13px;
  }
  .card-front {
    left: 82px; top: 139px;
    background: linear-gradient(180deg, var(--brand-blue) 0%, var(--brand-blue-dark) 100%);
  }
  .card-back {
    left: 600px; top: 138px;
    background: var(--card-white);
  }
  .firm-name {
    position: absolute;
    font-weight: 600;
    line-height: 1;
    white-space: nowrap;
  }
  .card-front .firm-name {
    left: 0; right: 0; top: 133px;
    text-align: center;
    font-size: 24px;
    color: #ffffff;
  }
  .card-back .firm-name {
    right: 34px; top: 58px;
    font-size: 19px;
    color: var(--brand-blue);
  }
  .accent-bar {
    position: absolute;
    left: 0; top: 43px;
    width: 13px; height: 49px;
    background: var(--brand-blue);
  }
  .holder { position: absolute; left: 30px; top: 48px; }
  .holder-name { font-size: 17px; font-weight: 600; color: var(--brand-blue); }
  .holder-title { font-size: 11px; color: var(--text-grey); margin-top: 2px; }
  .contact-list {
    position: absolute;
    left: 34px; top: 197px;
    list-style: none;
    font-size: 12.5px;
    color: var(--text-grey);
  }
  .contact-list li { display: flex; align-items: center; height: 17px; }
  .contact-list svg { width: 11px; height: 11px; margin-right: 8px; fill: var(--brand-blue); }
  .address {
    position: absolute;
    left: 30px; top: 257px;
    font-size: 12.5px;
    color: var(--text-grey);
  }
</style>
</head>
<body>
  <section class="card card-front">
    <p class="firm-name">Alvero Immigration Law</p>
  </section>

  <section class="card card-back">
    <div class="accent-bar"></div>
    <div class="holder">
      <p class="holder-name">John N. Smith</p>
      <p class="holder-title">Managing Director</p>
    </div>
    <p class="firm-name">Alvero Immigration Law</p>
    <ul class="contact-list">
      <li>
        <svg viewBox="0 0 12 12" aria-hidden="true"><path d="M1 4 Q6 0 11 4 L10 5.5 L8 5 L8 4 Q6 3 4 4 L4 5 L2 5.5 Z M2.5 6.5 H9.5 L10.5 11 H1.5 Z"/></svg>
        1300 418 552
      </li>
      <li>
        <svg viewBox="0 0 12 12" aria-hidden="true"><circle cx="6" cy="6" r="5.2" fill="none" stroke="#1f4a85" stroke-width="1.2"/><ellipse cx="6" cy="6" rx="2.2" ry="5.2" fill="none" stroke="#1f4a85" stroke-width="1"/><line x1="0.8" y1="6" x2="11.2" y2="6" stroke="#1f4a85" stroke-width="1"/></svg>
        www.alverolaw.example
      </li>
      <li>
        <svg viewBox="0 0 12 12" aria-hidden="true"><rect x="0.5" y="2.5" width="11" height="7.5" /><path d="M0.8 3 L6 7 L11.2 3" fill="none" stroke="#f7f7f7" stroke-width="1"/></svg>
        john.smith@alverolaw.example
      </li>
    </ul>
    <p class="address">123 XYZ Street, Country Name XYZ 12345</p>
  </section>
</body>
</html>
```